We need a brand logo for a range of health supplements we are launching.

The brand is called 'Mind Crate' The tagline for our brand is "The Entrepreneurs Supplement"

The brand is aimed at Entrepreneurs who would use our supplements to ultimately increase their brain power and turn them into more successful entrepreneurs.

As an additional note. The first product we launch is going to be a brain supplement that supports mental focus, promotes clarity and aids memory function. It's going to be called the Mind Crate Am Formula. This is a supplement which will be taken by entrepreneurs in the morning. The logo must therefore be suitable to incorporate it into the packaging design for our first product.

The product itself is a bottle of 60 capsules that comes in a box. (Therefore, it's a plastic bottle inside a cardboard box).

The bottle is black and comes with a black cap. I have attached an example of the bottle.

Also attached is the label template for the bottle. Everything that is displayed on the right and left hand side of the bottle must be visible. Everything in the middle can be deleted and re-designed except for 'Dietary supplement 60 Capsules' which must also be displayed.

Also attached is the box template. The box template is where all the creative design work should take place which can then be replicated onto the bottle.

The finished project should be a 3D render of the box and bottle side by side.

We would require the box and label templates to give to out manufacturer for printing.

Target Market(s)

Entrepreneurs

Industry/Entity Type

Health And Wellness

Logo Text

Mind Crate - The Entrepreneurs Supplement

Colors
3176b5
0255a3
85abd2
ffffff
e8e8e8
959595
f6f6f6
919191

Requirements
Must have
• This product must be aimed at entrepreneurs.
• The colur scheme should be Blue, Grey and White. The color schemes I have suggested

```html
<!DOCTYPE html>
<html lang="en">
<head>
<meta charset="utf-8">
<title>Mind Crate – The Entrepreneurs Supplement</title>
<link href="https://fonts.googleapis.com/css2?family=Quicksand:wght@500;600&family=Open+Sans:wght@400;600;700&family=Roboto+Condensed:wght@300;400&display=swap" rel="stylesheet">
<style>
:root{
  --blue:#1f74c0;
  --blue-deep:#0255a3;
  --blue-mid:#3176b5;
  --blue-soft:#85abd2;
  --white:#ffffff;
  --grey-light:#e8e8e8;
  --grey-pale:#f6f6f6;
  --grey:#959595;
  --ink:#1b1b1b;
}
*{box-sizing:border-box;margin:0;padding:0}
html,body{width:1200px;height:1029px;overflow:hidden;background:var(--white)}
body{position:relative;font-family:"Open Sans",sans-serif;color:var(--ink)}

/* brand lockup */
.brand{display:flex;align-items:center;gap:10px}
.brand-mark{flex:none;background:var(--blue-deep);border-radius:6px}
.brand-name{font-family:"Quicksand",sans-serif;font-weight:500;line-height:.9;color:var(--blue-deep);text-transform:uppercase}
.brand--hero{position:absolute;left:462px;top:114px}
.brand--hero .brand-mark{width:68px;height:68px}
.brand--hero .brand-name{font-size:41px}
.brand--light .brand-mark{background:var(--white)}
.brand--light .brand-name{color:var(--white)}

/* flat box */
.carton{position:absolute;left:110px;top:315px;width:390px;height:490px;display:flex}
.carton-side{width:150px;background:var(--blue);color:var(--white);padding:140px 12px 0;position:relative}
.carton-side p{font-size:6.2px;line-height:1.55;margin-bottom:8px;text-align:justify}
.carton-side b{font-weight:700}
.notice{background:var(--white);color:var(--ink);padding:4px 5px;font-size:5.6px;line-height:1.5}
.carton-side .brand{position:absolute;left:14px;bottom:26px;gap:5px}
.carton-side .brand-mark{width:28px;height:28px}
.carton-side .brand-name{font-size:17px}
.carton-front{flex:1;background:var(--blue);position:relative;overflow:hidden}
.front-card{position:absolute;left:14px;right:0;top:0;height:300px;background:var(--white);border-bottom-left-radius:130px}
.front-card .brand{position:absolute;left:24px;top:22px;gap:6px}
.front-card .brand-mark{width:44px;height:44px}
.front-card .brand-name{font-size:27px}
.tagline{position:absolute;right:16px;top:128px;text-align:right;font-family:"Roboto Condensed",sans-serif;font-weight:300;color:var(--ink);font-size:19px;line-height:1.35}
.tagline span{font-size:13px}
.brain-art{position:absolute;border-radius:50% 46% 44% 48%;background:radial-gradient(circle at 40% 40%,#7fc3f2,#1f6fc0 55%,#0b3e7a)}
.front-card .brain-art{left:44px;top:200px;width:120px;height:86px}
.benefits{position:absolute;left:24px;top:328px;list-style:none}
.benefits li{display:flex;align-items:center;margin-bottom:8px;font-family:"Roboto Condensed",sans-serif;font-weight:300;font-size:11.5px;color:var(--white)}
.benefits .num{width:38px;height:19px;background:var(--white);color:var(--blue-deep);font-size:15px;display:flex;align-items:center;justify-content:center;border-radius:3px 0 0 3px}
.benefits .pill{width:112px;height:19px;border:1.5px solid var(--white);border-left:0;border-radius:0 9px 9px 0;display:flex;align-items:center;justify-content:center}
.product-line{position:absolute;left:24px;color:var(--white);font-family:"Roboto Condensed",sans-serif;font-weight:300;line-height:1.2}
.product-line--caps{top:414px;font-size:9px;letter-spacing:1.4px;text-transform:uppercase}
.product-line--blend{top:434px;font-size:9.5px}
.count{position:absolute;left:24px;top:452px;color:var(--ink);font-family:"Roboto Condensed",sans-serif;font-weight:300;line-height:.95}
.count b{font-weight:300;font-size:17px;display:block}
.count span{font-size:12px;color:var(--blue-deep);text-transform:uppercase}

/* flat label */
.label{position:absolute;left:525px;top:478px;width:655px;height:326px;display:flex;background:var(--blue)}
.label-left{width:210px;color:var(--white);padding:22px 12px 0}
.label-left p{font-size:7.4px;line-height:1.5;margin-bottom:8px;text-align:justify}
.label-left .notice{font-size:7px}
.label-left .lot{margin-top:12px;width:90px;height:40px;border:1px solid var(--white)}
.label-front{width:255px;position:relative;overflow:hidden}
.label-front .brand{position:absolute;left:52px;top:14px;gap:6px}
.label-front .brand-mark{width:42px;height:42px}
.label-front .brand-name{font-size:26px}
.label-front .tagline{top:68px;right:20px;color:var(--white);font-size:17px;line-height:1.35}
.label-front .tagline span{font-size:12px}
.wave{position:absolute;left:0;top:122px;width:255px;height:128px}
.label-front .brain-art{left:6px;top:134px;width:96px;height:78px}
.claims{position:absolute;left:86px;top:142px;list-style:none}
.claims li{display:flex;align-items:center;gap:6px;height:26px;font-family:"Roboto Condensed",sans-serif;font-weight:300;font-size:10px;color:var(--ink)}
.claims li:nth-child(2){margin-left:-8px}
.claims li:nth-child(3){margin-left:-16px}
.claims .chip{border:1px solid var(--blue-deep);border-radius:0 8px 8px 0;padding:1px 8px}
.label-front .product-line--caps{top:256px;left:50px}
.label-front .product-line--blend{top:274px;left:50px}
.label-front .count{left:50px;top:292px}
.label-front .count b{font-size:16px}
.label-front .count span{font-size:12px}

.label-right{flex:1;background:var(--white);padding:14px 10px 0}
.facts{border:1.5px solid var(--ink)}
.facts h3{background:var(--blue);color:var(--white);font-family:"Quicksand",sans-serif;font-weight:600;font-size:15px;padding:2px 6px}
.facts .serve{font-size:7.5px;font-weight:700;padding:3px 6px;border-bottom:4px solid var(--ink);line-height:1.3}
.facts table{width:100%;border-collapse:collapse;font-size:7px}
.facts td{padding:2px 6px;vertical-align:top;border-bottom:1px solid var(--ink)}
.facts td.amt{text-align:right;white-space:nowrap;font-weight:700}
.facts .hd td{font-size:6px;text-align:right;border-bottom:2px solid var(--ink)}
.facts .dv{font-size:6.5px;font-weight:600;padding:2px 6px}
.other{font-size:6px;margin-top:6px;line-height:1.4}
.warn{font-size:6.4px;margin-top:6px;line-height:1.35;text-transform:uppercase}
.badges{display:flex;gap:10px;margin-top:8px}
.badges span{width:26px;height:26px;border-radius:50%;background:var(--grey-light);border:1px solid var(--grey)}
</style>
</head>
<body>

<div class="brand brand--hero">
  <span class="brand-mark"></span>
  <span class="brand-name">Mind<br>Crate</span>
</div>

<section class="carton" aria-label="Carton artwork">
  <div class="carton-side">
    <p><b>SUGGESTED USE:</b> As a dietary supplement, take one (1) capsule daily. Do not exceed two (2) capsules per day, or take as directed by your health care professional.</p>
    <p><b>CAUTION:</b> Do not exceed recommended dose. St. John's Wort may contribute to photosensitivity resulting in skin irritation and redness in persons exposed to strong sunlight or tanning booths. Avoid in patients at risk of bleeding, taking anticoagulants, or with clotting disorders, based on case reports of bleeding. Discontinue use 2-3 weeks prior to some surgical and dental procedures due to increased risk of bleeding. Use cautiously in patients with history of seizure, based on reports of seizure due to Ginkgo seed ingestion. Avoid use in couples who are trying to conceive.</p>
    <div class="notice">*These statements have not been evaluated by the Food and Drug Administration. This product is not intended to diagnose, treat, cure or prevent any disease.</div>
    <div class="brand brand--light"><span class="brand-mark"></span><span class="brand-name">Mind<br>Crate</span></div>
  </div>
  <div class="carton-front">
    <div class="front-card">
      <div class="brand"><span class="brand-mark"></span><span class="brand-name">Mind<br>Crate</span></div>
      <p class="tagline"><span>THE</span> ENTREPRENEURS<br>SUPPLEMENT</p>
      <div class="brain-art" role="img" aria-label="Glowing blue illustration of a human brain"></div>
    </div>
    <ol class="benefits">
      <li><span class="num">1.</span><span class="pill">Supports Mental Focus</span></li>
      <li><span class="num">2.</span><span class="pill">Promotes Clarity*</span></li>
      <li><span class="num">3.</span><span class="pill">Memory Function Aid*</span></li>
    </ol>
    <p class="product-line product-line--caps">Alertness &amp; Concentration</p>
    <p class="product-line product-line--blend">Super Strength Synergistic Blend</p>
    <p class="count"><b>60</b><span>Veg Capsules</span></p>
  </div>
</section>

<section class="label" aria-label="Bottle label artwork">
  <div class="label-left">
    <p><b>SUGGESTED USE:</b> As a dietary supplement, take one (1) capsule daily. Do not exceed two (2) capsules per day, or take as directed by your health care professional.</p>
    <p><b>CAUTION:</b> Do not exceed recommended dose. St. John's Wort may contribute to photosensitivity resulting in skin irritation and redness in persons exposed to strong sunlight or tanning booths. Avoid in patients at risk of bleeding, taking anticoagulants, or with clotting disorders. Discontinue use 2-3 weeks prior to some surgical and dental procedures due to increased risk of bleeding. Use cautiously in patients with history of seizure. Avoid use in couples who are trying to conceive.</p>
    <div class="notice">*These statements have not been evaluated by the Food and Drug Administration. This product is not intended to diagnose, treat, cure or prevent any disease.</div>
    <div class="lot"></div>
  </div>

  <div class="label-front">
    <div class="brand brand--light"><span class="brand-mark"></span><span class="brand-name">Mind<br>Crate</span></div>
    <p class="tagline"><span>THE</span> ENTREPRENEURS<br>SUPPLEMENT</p>
    <svg class="wave" viewBox="0 0 255 128" aria-hidden="true">
      <path d="M0 10 Q0 0 40 0 H255 V128 H60 Q0 128 0 84 Z" fill="#ffffff"/>
    </svg>
    <div class="brain-art" role="img" aria-label="Glowing blue illustration of a human brain"></div>
    <ul class="claims">
      <li><svg width="42" height="12" viewBox="0 0 42 12" aria-hidden="true"><g fill="none" stroke="#0255a3" stroke-width="3"><path d="M8 1 2 6l6 5M17 1l-6 5 6 5M26 1l-6 5 6 5M35 1l-6 5 6 5"/></g></svg><span class="chip">Supports Mental Focus</span></li>
      <li><svg width="42" height="12" viewBox="0 0 42 12" aria-hidden="true"><g fill="none" stroke="#0255a3" stroke-width="3"><path d="M8 1 2 6l6 5M17 1l-6 5 6 5M26 1l-6 5 6 5M35 1l-6 5 6 5"/></g></svg><span class="chip">Promotes Clarity*</span></li>
      <li><svg width="42" height="12" viewBox="0 0 42 12" aria-hidden="true"><g fill="none" stroke="#0255a3" stroke-width="3"><path d="M8 1 2 6l6 5M17 1l-6 5 6 5M26 1l-6 5 6 5M35 1l-6 5 6 5"/></g></svg><span class="chip">Memory Function Aid*</span></li>
    </ul>
    <p class="product-line product-line--caps">Alertness &amp; Concentration</p>
    <p class="product-line product-line--blend">Super Strength Synergistic Blend</p>
    <p class="count"><b>60</b><span>Veg Capsules</span></p>
  </div>

  <div class="label-right">
    <div class="facts">
      <h3>Supplement Facts</h3>
      <p class="serve">Serving Size: 1 Capsule<br>Servings Per Container: 60</p>
      <table>
        <tr class="hd"><td colspan="2">Amount Per Serving &nbsp;%DV</td></tr>
        <tr><td><b>Ginkovex™</b><br><b>Ginkgo Biloba</b> (as 24% extract)</td><td class="amt">50 mg †</td></tr>
        <tr><td><b>Proprietary Formula</b><br><b>St. John's Wort</b> (as .3% extract), <b>Glutamine</b> (as L-Glutamine Hydrochloride), <b>Phosphatidylserine Complex, Bacopa Monnier</b> (20% Bacosides), <b>Dimethylaminoethanol Bitartrate, Acetyl-L Carnitine</b></td><td class="amt">727 mg †</td></tr>
      </table>
      <p class="dv">† % Daily Value (DV) not established</p>
    </div>
    <p class="other"><b>Other Ingredients:</b> Gelatin, Magnesium Stearate, Di-Calcium Phosphate.</p>
    <p class="warn">Keep out of the reach of children. Do not use if safety seal is damaged or missing. Store at room temperature.</p>
    <div class="badges" aria-hidden="true"><span></span><span></span><span></span><span></span></div>
  </div>
</section>

</body>
</html>
```